Customer Dashboard Design for Email Security SaaS

Mailvarden is a commercial email spam filter offered as a SaaS product, built and operated by a small German hosting provider. It protects business email accounts against spam, phishing, scam, and viruses using a multilayer filtering pipeline that combines traditional spam detection with AI-powered classification. The product runs entirely on German infrastructure, ensuring data sovereignty for European customers.

We need a complete redesign of the customer-facing dashboard. This is the web application where paying customers manage their email filtering: view their mail log, check quarantined emails, manage allow/blocklists, configure their settings, and handle their subscription. It is the primary touchpoint between Mailvarden and its customers.

Our customers are system administrators, IT managers at small-to-medium businesses, and operators of small hosting providers. They are technically competent but not designers. They expect professional, efficient tools that respect their time. They typically manage 10–500 email accounts and check the dashboard a few times per week, with heavier use during spam incidents.

We have attached the current mockups which really need to be replaced with something good looking.

Target Market(s)

System administrators, IT managers at small-to-medium businesses, and operators of small hosting providers.

Industry/Entity Type

SaaS

Number of Pages Required

5+ page

```html
<!DOCTYPE html>
<html lang="en">
<head>
<meta charset="utf-8">
<title>Mailvarden – Customer Dashboard</title>
<link href="https://fonts.googleapis.com/css2?family=Inter:wght@400;500;600;700&display=swap" rel="stylesheet">
<style>
:root{
  --page:#ffffff;
  --shell:#121212;
  --main:#1a1a1a;
  --card:#232323;
  --card-2:#2a2a2a;
  --line:#3a3a3a;
  --text:#f2f2f2;
  --muted:#a3a3a3;
  --green:#1f6b45;
  --green-bright:#22c55e;
  --ham:#22c55e;
  --phish:#ef4444;
  --virus:#6366f1;
  --news:#f59e0b;
  --spam:#f97316;
  --yellow:#b8901a;
  --indigo:#2a2a7a;
  --orange:#c2410c;
}
*{box-sizing:border-box;margin:0;padding:0}
html,body{width:1200px;height:452px;overflow:hidden;background:var(--page)}
body{font-family:"Inter",sans-serif;color:var(--text);position:relative}
.abs{position:absolute}
.panel{position:absolute;background:var(--shell);border-radius:14px;overflow:hidden}
.panel--dash{left:6px;top:4px;width:594px;height:439px}
.panel--log{left:601px;top:5px;width:594px;height:350px}
.main{position:absolute;left:105px;top:4px;background:var(--main);border-radius:12px}
.panel--dash .main{width:486px;height:430px}
.panel--log .main{width:484px;height:337px}
.brand{position:absolute;left:0;width:105px;text-align:center;font-size:11px;font-weight:500;letter-spacing:.2px}
.nav{position:absolute;left:6px;width:93px;height:16px;border-radius:4px;display:flex;align-items:center;gap:4px;padding-left:5px;font-size:6.5px;color:var(--muted)}
.nav svg{width:8px;height:8px;stroke:currentColor;fill:none;stroke-width:1.6}
.nav--active{background:var(--green);color:var(--text)}
.page-title{position:absolute;left:115px;font-size:8.5px;font-weight:600}
.page-sub{position:absolute;left:115px;font-size:6.5px;color:var(--muted)}
.divider{position:absolute;left:115px;height:1px;background:var(--line)}
.bell{position:absolute;width:15px;height:15px;border:1px solid #777;border-radius:50%;display:flex;align-items:center;justify-content:center}
.bell svg{width:8px;height:8px;stroke:#ddd;fill:none;stroke-width:1.5}
.bell b{position:absolute;right:-3px;top:-3px;width:8px;height:8px;border-radius:50%;background:var(--green);font-size:5px;display:flex;align-items:center;justify-content:center;font-weight:500}
.avatar{position:absolute;width:16px;height:16px;border-radius:50%;background:linear-gradient(135deg,#c9a58c,#7a4a3a)}
.chev{position:absolute;width:6px;height:6px;stroke:#ddd;fill:none;stroke-width:1.6}
.card{position:absolute;background:var(--card);border-radius:6px}
.label{font-size:6.8px;color:#dcdcdc;font-weight:500}
.icon-box{position:absolute;width:21px;height:21px;border-radius:4px;display:flex;align-items:center;justify-content:center}
.icon-box svg{width:11px;height:11px;fill:none;stroke-width:1.5}
.stat .label{position:absolute;left:7px;top:13px}
.stat .num{position:absolute;left:7px;top:29px;font-size:10px;font-weight:600}
.stat .period{position:absolute;left:7px;top:51px;font-size:6.5px;color:var(--muted)}
.btn-green{position:absolute;background:var(--green);border-radius:3px;font-size:6.5px;font-weight:500;display:flex;align-items:center;justify-content:center;gap:3px}
.select{position:absolute;background:#1b1b1b;border-radius:4px;font-size:6.5px;display:flex;align-items:center;justify-content:space-between;padding:0 6px}
.select svg{width:5px;height:5px;stroke:#ddd;fill:none;stroke-width:1.8}
.link-card .title{position:absolute;left:10px;top:7px;font-size:6.8px;font-weight:500}
.link-card .desc{position:absolute;left:10px;top:19px;font-size:5.6px;color:var(--muted);line-height:8px;width:140px}
.link-card svg{position:absolute;right:9px;top:17px;width:7px;height:7px;stroke:#eee;fill:none;stroke-width:1.8}
.search{position:absolute;left:115px;top:47px;width:200px;height:16px;background:#232323;border-radius:4px;display:flex;align-items:center;gap:4px;padding-left:12px;font-size:5.6px;color:#cfcfcf}
.search svg{width:7px;height:7px;stroke:#ddd;fill:none;stroke-width:1.7}
.filter{position:absolute;left:489px;top:47px;width:85px;height:17px;background:#232323;border-radius:4px;display:flex;align-items:center;gap:8px;padding-left:10px;font-size:6.5px}
.filter svg{width:8px;height:8px;stroke:#ddd;fill:none;stroke-width:1.5}
.table-card{position:absolute;left:115px;top:93px;width:469px;height:233px;background:var(--card);border-radius:6px;overflow:hidden}
.thead{position:absolute;left:3px;top:7px;width:466px;height:18px;background:#1d1d1d;font-size:5.8px;font-weight:500}
.row{position:absolute;left:0;width:469px;height:22px;border-bottom:1px solid #3d3d3d;font-size:5.8px}
.cell{position:absolute;top:50%;transform:translateY(-50%);white-space:nowrap}
.c-num{left:21px}
.c-time{left:48px;font-weight:500}
.c-send{left:139px;color:#cfcfcf}
.c-rcpt{left:236px;color:#cfcfcf}
.c-verdict{left:327px}
.c-subj{left:400px;font-weight:500}
.thead .cell{color:#eee}
.badge{display:inline-flex;align-items:center;gap:2px;height:11px;padding:0 5px;border:1px solid currentColor;border-radius:3px;font-size:5.8px}
.badge i{width:3.5px;height:3.5px;border:.8px solid currentColor;border-radius:50%;display:inline-block}
.b-ham{color:var(--ham)}.b-phish{color:var(--phish)}.b-virus{color:#7c7ff5}.b-news{color:var(--news)}.b-spam{color:var(--spam)}
.scroll{position:absolute;left:3px;top:229px;width:153px;height:2px;border-radius:2px;background:#e5e5e5}
.sr{position:absolute;width:1px;height:1px;overflow:hidden;clip:rect(0 0 0 0)}
</style>
</head>
<body>

<svg class="sr" aria-hidden="true">
  <symbol id="i-grid" viewBox="0 0 16 16"><rect x="2" y="2" width="5" height="5" rx="1"/><rect x="9" y="2" width="5" height="5" rx="1"/><rect x="2" y="9" width="5" height="5" rx="1"/><rect x="9" y="9" width="5" height="5" rx="1"/></symbol>
  <symbol id="i-mail" viewBox="0 0 16 16"><rect x="2" y="3.5" width="12" height="9" rx="1.5"/><path d="M2.5 4.5 8 9l5.5-4.5"/></symbol>
  <symbol id="i-shield" viewBox="0 0 16 16"><path d="M8 1.8 13 3.8v4c0 3-2.2 5.2-5 6.4-2.8-1.2-5-3.4-5-6.4v-4z"/></symbol>
  <symbol id="i-dollar" viewBox="0 0 16 16"><circle cx="8" cy="8" r="6"/><path d="M10 6c0-1-1-1.5-2-1.5S6 5 6 6s1 1.3 2 1.5 2 .6 2 1.6-1 1.5-2 1.5-2-.5-2-1.5M8 3.8v8.4"/></symbol>
  <symbol id="i-user" viewBox="0 0 16 16"><circle cx="7" cy="5" r="3"/><path d="M1.5 14c.5-3 2.8-4.5 5.5-4.5M10 10.5l4 3.5M14 10.5l-4 3.5"/></symbol>
  <symbol id="i-doc" viewBox="0 0 16 16"><rect x="3" y="2" width="10" height="12" rx="1.5"/><path d="M5.5 6h5M5.5 9h5M5.5 11.5h3"/></symbol>
  <symbol id="i-gear" viewBox="0 0 16 16"><circle cx="8" cy="8" r="2.2"/><path d="M8 1.5v2M8 12.5v2M1.5 8h2M12.5 8h2M3.4 3.4l1.4 1.4M11.2 11.2l1.4 1.4M3.4 12.6l1.4-1.4M11.2 4.8l1.4-1.4"/></symbol>
  <symbol id="i-bell" viewBox="0 0 16 16"><path d="M4 11V7a4 4 0 0 1 8 0v4l1.2 1.5H2.8zM6.5 14h3"/></symbol>
  <symbol id="i-chev" viewBox="0 0 10 10"><path d="M2 3.5 5 6.5 8 3.5"/></symbol>
  <symbol id="i-arrow" viewBox="0 0 10 10"><path d="M1.5 5h7M5.5 2l3 3-3 3"/></symbol>
  <symbol id="i-search" viewBox="0 0 16 16"><circle cx="7" cy="7" r="4.5"/><path d="m10.5 10.5 3.5 3.5"/></symbol>
  <symbol id="i-sliders" viewBox="0 0 16 16"><path d="M2 4h12M2 8h12M2 12h12"/><circle cx="10" cy="4" r="1.5"/><circle cx="5" cy="8" r="1.5"/><circle cx="9" cy="12" r="1.5"/></symbol>
  <symbol id="i-trend" viewBox="0 0 16 16"><path d="M1.5 12 6 7.5l3 3L14.5 5M10.5 5h4v4"/></symbol>
  <symbol id="i-bug" viewBox="0 0 16 16"><ellipse cx="8" cy="9" rx="3.5" ry="4.5"/><path d="M8 4.5v9M2 9h2.5M11.5 9H14M3 5l2 1.5M13 5l-2 1.5M3 13l2-1.5M13 13l-2-1.5"/></symbol>
  <symbol id="i-inbox" viewBox="0 0 16 16"><path d="M2 9h3.5l1 2h3l1-2H14v4H2zM2 9l2-5h8l2 5M6 6.5l2 2 2-2"/></symbol>
</svg>

<!-- ========== Dashboard screen ========== -->
<section class="panel panel--dash">
  <div class="brand" style="top:20px">Mailvarden</div>
  <div class="nav nav--active" style="top:41px"><svg><use href="#i-grid"/></svg>Dashboard</div>
  <div class="nav" style="top:62px"><svg><use href="#i-mail"/></svg>Mail log</div>
  <div class="nav" style="top:83px"><svg><use href="#i-shield"/></svg>Quarantine</div>
  <div class="nav" style="top:104px"><svg><use href="#i-mail"/></svg>Mailboxes</div>
  <div class="nav" style="top:125px"><svg><use href="#i-dollar"/></svg>Allowlist</div>
  <div class="nav" style="top:147px"><svg><use href="#i-user"/></svg>Blocklist</div>
  <div class="nav" style="top:168px"><svg><use href="#i-doc"/></svg>Billing</div>
  <div class="nav" style="top:278px"><svg><use href="#i-gear"/></svg>Settings</div>

  <div class="main" style="left:105px"></div>

  <div class="page-title" style="top:10px">Welcome Back, Jonas</div>
  <div class="page-sub" style="top:23px">Thu April 15, 2026</div>
  <div class="divider" style="top:36px;width:471px"></div>
  <div class="bell" style="left:529px;top:13px"><svg><use href="#i-bell"/></svg><b>2</b></div>
  <div class="avatar" role="img" aria-label="User profile photo" style="left:556px;top:13px"></div>
  <svg class="chev" style="left:577px;top:19px"><use href="#i-chev"/></svg>

  <div class="page-title" style="top:47px;font-size:9px">Dashboard</div>

  <div class="card" style="left:115px;top:64px;width:463px;height:42px">
    <div class="abs label" style="left:10px;top:8px;display:flex;align-items:center;gap:4px"><svg style="width:8px;height:8px;stroke:#e0b020;fill:none;stroke-width:1.6"><use href="#i-mail"/></svg>Total Emails Filtered</div>
    <div class="abs" style="left:10px;top:21px;display:flex;align-items:center;gap:5px">
      <span style="font-size:10.5px;font-weight:600">10,230</span>
      <svg style="width:8px;height:8px;stroke:var(--green-bright);fill:none;stroke-width:1.6"><use href="#i-trend"/></svg>
      <span style="font-size:6.5px;color:var(--green-bright)">8.5% Up from last month</span>
    </div>
  </div>

  <div class="card stat" style="left:115px;top:113px;width:107px;height:65px">
    <div class="label">Spam Blocked</div><div class="num">20</div><div class="period">Last 7 days</div>
    <div class="icon-box" style="left:80px;top:6px;background:var(--green)"><svg style="stroke:#9ef0b8"><use href="#i-user"/></svg></div>
  </div>
  <div class="card stat" style="left:234px;top:113px;width:107px;height:65px">
    <div class="label">Phishing Detected</div><div class="num">07</div><div class="period">Last 7 days</div>
    <div class="icon-box" style="left:80px;top:6px;background:var(--yellow)"><svg style="stroke:#fff2b0"><use href="#i-inbox"/></svg></div>
  </div>
  <div class="card stat" style="left:352px;top:113px;width:107px;height:65px">
    <div class="label">Viruses Caught</div><div class="num">08</div><div class="period">Last 7 days</div>
    <div class="icon-box" style="left:80px;top:6px;background:var(--indigo)"><svg style="stroke:#7c7ff5"><use href="#i-bug"/></svg></div>
  </div>
  <div class="card stat" style="left:470px;top:113px;width:108px;height:65px">
    <div class="label">Newsletter Sorted</div><div class="num">56</div><div class="period">Last 7 days</div>
    <div class="icon-box" style="left:81px;top:6px;background:var(--orange)"><svg style="stroke:#ffd0b8"><use href="#i-inbox"/></svg></div>
  </div>

  <div class="card" style="left:115px;top:186px;width:463px;height:42px">
    <div class="icon-box" style="left:10px;top:10px;background:var(--orange)"><svg style="stroke:#ffd0b8"><use href="#i-mail"/></svg></div>
    <div class="abs" style="left:38px;top:11px;font-size:8.5px;font-weight:600;letter-spacing:.3px">32 Emails</div>
    <div class="abs" style="left:38px;top:24px;font-size:6.5px;color:#cfcfcf">Currently in quarantine</div>
    <div class="btn-green" style="left:377px;top:14px;width:73px;height:14px">Review Quarantine <svg style="width:5px;height:5px;stroke:#fff;fill:none;stroke-width:1.8;transform:rotate(-90deg)"><use href="#i-chev"/></svg></div>
  </div>

  <div class="card" style="left:115px;top:235px;width:463px;height:140px">
    <div class="abs label" style="left:7px;top:6px;font-size:7.5px;color:var(--text)">Email Activity</div>
    <div class="select" style="left:353px;top:6px;width:46px;height:14px">2026<svg><use href="#i-chev"/></svg></div>
    <div class="select" style="left:407px;top:6px;width:46px;height:14px">Yearly<svg><use href="#i-chev"/></svg></div>
    <svg class="abs" style="left:0;top:0" width="463" height="140" viewBox="0 0 463 140" role="img" aria-label="Email activity line chart by month">
      <defs>
        <linearGradient id="g-total" x1="0" y1="0" x2="0" y2="1"><stop offset="0" stop-color="#3b8a63" stop-opacity=".45"/><stop offset="1" stop-color="#3b8a63" stop-opacity=".05"/></linearGradient>
        <linearGradient id="g-spam" x1="0" y1="0" x2="0" y2="1"><stop offset="0" stop-color="#5a5ad0" stop-opacity=".55"/><stop offset="1" stop-color="#5a5ad0" stop-opacity=".1"/></linearGradient>
      </defs>
      <g stroke="#555" stroke-width=".5">
        <line x1="26" y1="27" x2="453" y2="27"/><line x1="26" y1="47.4" x2="453" y2="47.4"/><line x1="26" y1="67.8" x2="453" y2="67.8"/><line x1="26" y1="88.2" x2="453" y2="88.2"/><line x1="26" y1="108.6" x2="453" y2="108.6"/>
      </g>
      <g fill="#bbb" font-size="4" font-family="Inter, sans-serif">
        <text x="8" y="28.5">1500</text><text x="8" y="49">1200</text><text x="10" y="69.3">900</text><text x="10" y="89.7">600</text><text x="10" y="110">300</text>
      </g>
      <path fill="url(#g-spam)" d="M39,80 C60.5,80 60.5,100 82,100 C103.5,100 103.5,63 125,63 C146.5,63 146.5,100 168,100 C189.5,100 189.5,85 211,85 C232,85 232,37 253,37 C274.5,37 274.5,96 296,96 C317.5,96 317.5,35 339,35 C360.5,35 360.5,73 382,73 C403.5,73 403.5,46 425,46 L425,108.6 L39,108.6 Z"/>
      <path fill="url(#g-total)" d="M39,61 C60.5,61 60.5,98 82,98 C103.5,98 103.5,59 125,59 C146.5,59 146.5,100 168,100 C189.5,100 189.5,73 211,73 C232,73 232,55 253,55 C274.5,55 274.5,94 296,94 C317.5,94 317.5,78 339,78 C360.5,78 360.5,96 382,96 C403.5,96 403.5,39 425,39 L425,108.6 L39,108.6 Z"/>
      <path fill="none" stroke="#6e6ee6" stroke-width=".8" d="M39,80 C60.5,80 60.5,100 82,100 C103.5,100 103.5,63 125,63 C146.5,63 146.5,100 168,100 C189.5,100 189.5,85 211,85 C232,85 232,37 253,37 C274.5,37 274.5,96 296,96 C317.5,96 317.5,35 339,35 C360.5,35 360.5,73 382,73 C403.5,73 403.5,46 425,46"/>
      <path fill="none" stroke="#5fc48f" stroke-width=".8" d="M39,61 C60.5,61 60.5,98 82,98 C103.5,98 103.5,59 125,59 C146.5,59 146.5,100 168,100 C189.5,100 189.5,73 211,73 C232,73 232,55 253,55 C274.5,55 274.5,94 296,94 C317.5,94 317.5,78 339,78 C360.5,78 360.5,96 382,96 C403.5,96 403.5,39 425,39"/>
      <g fill="#8ee6b4" stroke="#2f6e4c" stroke-width=".6">
        <circle cx="39" cy="61" r="1.6"/><circle cx="82" cy="98" r="1.6"/><circle cx="125" cy="59" r="1.6"/><circle cx="168" cy="100" r="1.6"/><circle cx="211" cy="73" r="1.6"/><circle cx="253" cy="55" r="1.6"/><circle cx="296" cy="94" r="1.6"/><circle cx="339" cy="78" r="1.6"/><circle cx="382" cy="96" r="1.6"/><circle cx="425" cy="39" r="1.6"/>
      </g>
      <g fill="#a5a5ff" stroke="#3b3ba0" stroke-width=".6">
        <circle cx="39" cy="80" r="1.6"/><circle cx="82" cy="100" r="1.6"/><circle cx="125" cy="63" r="1.6"/><circle cx="168" cy="100" r="1.6"/><circle cx="211" cy="85" r="1.6"/><circle cx="253" cy="37" r="1.6"/><circle cx="296" cy="96" r="1.6"/><circle cx="339" cy="35" r="1.6"/><circle cx="382" cy="73" r="1.6"/><circle cx="425" cy="46" r="1.6"/>
      </g>
      <g fill="#bbb" font-size="4.6" font-family="Inter, sans-serif" text-anchor="middle">
        <text x="39" y="122">Jan</text><text x="74.5" y="122">Feb</text><text x="110" y="122">Mar</text><text x="145.5" y="122">Apr</text><text x="181" y="122">May</text><text x="216.5" y="122">Jun</text><text x="251" y="122">Jul</text><text x="285.5" y="122">Aug</text><text x="321" y="122">Sep</text><text x="356.5" y="122">Oct</text><text x="392" y="122">Nov</text><text x="428" y="122">Dec</text>
      </g>
      <g font-size="4.6" font-family="Inter, sans-serif" fill="#bbb">
        <line x1="122" y1="133" x2="129" y2="133" stroke="#3fa06c" stroke-width=".9"/><text x="139" y="135">Total</text>
        <line x1="174" y1="133" x2="181" y2="133" stroke="#6e6ee6" stroke-width=".9"/><text x="184" y="135">Spam</text>
        <line x1="214" y1="133" x2="221" y2="133" stroke="#ef4444" stroke-width=".9"/><text x="224" y="135">Phishing</text>
        <line x1="267" y1="133" x2="274" y2="133" stroke="#eab308" stroke-width=".9"/><text x="277" y="135">Virus</text>
        <line x1="305" y1="133" x2="312" y2="133" stroke="#ef4444" stroke-width=".9"/><text x="315" y="135">Newsletter</text>
      </g>
    </svg>
  </div>

  <div class="card link-card" style="left:115px;top:382px;width:227px;height:41px">
    <div class="title">View Mail Log</div>
    <div class="desc">Browse all processed emails and see detailed classifications</div>
    <svg><use href="#i-arrow"/></svg>
  </div>
  <div class="card link-card" style="left:350px;top:382px;width:228px;height:41px">
    <div class="title">Manage Settings</div>
    <div class="desc">Configure retention periods, anonymization, and oversize behaviour</div>
    <svg><use href="#i-arrow"/></svg>
  </div>
</section>

<!-- ========== Mail log screen ========== -->
<section class="panel panel--log">
  <div class="brand" style="top:19px">Mailvarden</div>
  <div class="nav" style="top:44px"><svg><use href="#i-grid"/></svg>Dashboard</div>
  <div class="nav nav--active" style="top:66px"><svg><use href="#i-mail"/></svg>Mail log</div>
  <div class="nav" style="top:88px"><svg><use href="#i-shield"/></svg>Quarantine</div>
  <div class="nav" style="top:109px"><svg><use href="#i-mail"/></svg>Mailboxes</div>
  <div class="nav" style="top:130px"><svg><use href="#i-dollar"/></svg>Allowlist</div>
  <div class="nav" style="top:151px"><svg><use href="#i-user"/></svg>Blocklist</div>
  <div class="nav" style="top:278px"><svg><use href="#i-gear"/></svg>Settings</div>

  <div class="main"></div>

  <div class="page-title" style="top:10px">Mail Log</div>
  <div class="page-sub" style="top:23px">Complete history of all processed emails with detailed classification</div>
  <div class="divider" style="top:36px;width:469px;left:105px;width:484px"></div>
  <div class="bell" style="left:527px;top:14px"><svg><use href="#i-bell"/></svg><b>2</b></div>
  <div class="avatar" role="img" aria-label="User profile photo" style="left:555px;top:14px"></div>
  <svg class="chev" style="left:576px;top:20px"><use href="#i-chev"/></svg>

  <div class="search"><svg><use href="#i-search"/></svg>Search by sender, recipient, or subject.....</div>
  <div class="filter"><svg><use href="#i-sliders"/></svg>By verdict<svg style="width:5px;height:5px;stroke-width:1.8"><use href="#i-chev"/></svg></div>
  <div class="abs" style="left:115px;top:74px;font-size:6.8px;font-weight:500">Showing 9 of 9 emails</div>

  <div class="table-card">
    <div class="thead">
      <span class="cell" style="left:61px">Timestamp</span>
      <span class="cell" style="left:161px">Sender</span>
      <span class="cell" style="left:254px">Recipient</span>
      <span class="cell" style="left:338px">Verdict</span>
      <span class="cell" style="left:443px">Subject</span>
    </div>

    <div class="row" style="top:25px"><span class="cell c-num">1</span><span class="cell c-time">2026-04-12&nbsp;&nbsp;12:23:34</span><span class="cell c-send">anna@brightkeel.io</span><span class="cell c-rcpt">offers@dealpost.example</span><span class="cell c-verdict"><span class="badge b-ham"><i></i>Ham</span></span><span class="cell c-subj">Daily Digest: Top Tech News</span></div>
    <div class="row" style="top:47px"><span class="cell c-num">2</span><span class="cell c-time">2026-04-12&nbsp;&nbsp;12:23:34</span><span class="cell c-send">offers@dealpost.example</span><span class="cell c-rcpt">anna@brightkeel.io</span><span class="cell c-verdict"><span class="badge b-phish"><i></i>Phishing</span></span><span class="cell c-subj">Urgent: Verify your account</span></div>
    <div class="row" style="top:69px"><span class="cell c-num">3</span><span class="cell c-time">2026-04-12&nbsp;&nbsp;12:23:34</span><span class="cell c-send">anna@brightkeel.io</span><span class="cell c-rcpt">offers@dealpost.example</span><span class="cell c-verdict"><span class="badge b-virus"><i></i>Virus</span></span><span class="cell c-subj">Daily Digest: Top Tech News</span></div>
    <div class="row" style="top:91px"><span class="cell c-num">4</span><span class="cell c-time">2026-04-12&nbsp;&nbsp;12:23:34</span><span class="cell c-send">offers@dealpost.example</span><span class="cell c-rcpt">anna@brightkeel.io</span><span class="cell c-verdict"><span class="badge b-news"><i></i>Newsletter</span></span><span class="cell c-subj">Urgent: Verify your account</span></div>
    <div class="row" style="top:113px"><span class="cell c-num">5</span><span class="cell c-time">2026-04-12&nbsp;&nbsp;12:23:34</span><span class="cell c-send">offers@dealpost.example</span><span class="cell c-rcpt">offers@dealpost.example</span><span class="cell c-verdict"><span class="badge b-ham"><i></i>Ham</span></span><span class="cell c-subj">Daily Digest: Top Tech News</span></div>
    <div class="row" style="top:135px"><span class="cell c-num">6</span><span class="cell c-time">2026-04-12&nbsp;&nbsp;12:23:34</span><span class="cell c-send">anna@brightkeel.io</span><span class="cell c-rcpt">anna@brightkeel.io</span><span class="cell c-verdict"><span class="badge b-phish"><i></i>Phishing</span></span><span class="cell c-subj">Urgent: Verify your account</span></div>
    <div class="row" style="top:157px"><span class="cell c-num">7</span><span class="cell c-time">2026-04-12&nbsp;&nbsp;12:23:34</span><span class="cell c-send">offers@dealpost.example</span><span class="cell c-rcpt">offers@dealpost.example</span><span class="cell c-verdict"><span class="badge b-virus"><i></i>Virus</span></span><span class="cell c-subj">Daily Digest: Top Tech News</span></div>
    <div class="row" style="top:179px"><span class="cell c-num">8</span><span class="cell c-time">2026-04-12&nbsp;&nbsp;12:23:34</span><span class="cell c-send">anna@brightkeel.io</span><span class="cell c-rcpt">offers@dealpost.example</span><span class="cell c-verdict"><span class="badge b-news"><i></i>Newsletter</span></span><span class="cell c-subj">Urgent: Verify your account</span></div>
    <div class="row" style="top:201px;border-bottom:none"><span class="cell c-num">9</span><span class="cell c-time">2026-04-12&nbsp;&nbsp;12:23:34</span><span class="cell c-send">offers@dealpost.example</span><span class="cell c-rcpt">anna@brightkeel.io</span><span class="cell c-verdict"><span class="badge b-spam"><i></i>Spam</span></span><span class="cell c-subj">Daily Digest: Top Tech News</span></div>

    <div class="scroll"></div>
  </div>
</section>

</body>
</html>
```